Dental Medical History Form - Content provided

Design a medical history form for a dental practice. Content is provided so all that is needed is the formatting to make it look great and easy to read.

"Patient Information" to include all information contained in top portion of the "Patient Medical History Form" docx file.

"Medical History" should follow the formatting and content of the "Exact Medical History" file as this is what the entry fields look like in our practice software and so we would like it to match.

1st page - Patient info, allergies, medications, antibiotics, joint replacement, pregnancy.

2nd page - Do you have, or have you had, any of the following? . . . . . . .
Updates

Project Deadline Extended Reason: Picked too short of a deadline to start (2 days) Added Monday, February 13, 2017

Target Market(s)

All ages but must be clear enough for elderly to read. Use as much space as possible to keep font size bigger yet keep to two pages

Industry/Entity Type

Dental

Font styles to use
Sans Serif

Requirements
Must have
• All content provided
• Our logo at the top (file provided)
• Century Gothic Font
• Limit to two pages

```html
<!DOCTYPE html>
<html lang="en">
<head>
<meta charset="utf-8">
<title>Harbour Dental – Confidential Medical History</title>
<link href="https://fonts.googleapis.com/css2?family=Didact+Gothic&display=swap" rel="stylesheet">
<style>
  :root{
    --ink:#2f2f2f;
    --brand:#46525c;
    --rule:#9a9a9a;
    --paper:#ffffff;
  }
  html,body{margin:0;padding:0;overflow:hidden;background:var(--paper);}
  .form-page{position:relative;width:854px;height:1200px;overflow:hidden;background:var(--paper);
    font-family:"Didact Gothic","Century Gothic",sans-serif;color:var(--ink);font-size:17px;}
  .at{position:absolute;transform:translateY(-50%);white-space:nowrap;line-height:1;}
  .brand-name{position:absolute;left:32px;top:68px;margin:0;color:var(--brand);font-size:46px;font-weight:400;line-height:1;}
  .practice-address{position:absolute;right:32px;top:47px;text-align:right;font-size:17.5px;line-height:21.6px;color:var(--ink);font-style:normal;}
  .form-title{font-size:22.3px;margin:0;font-weight:400;}
  .section-title{font-size:17.5px;margin:0;font-weight:400;}
  .gp{font-size:18px;}
  .question{font-size:18px;margin:0;}
  .hint{font-size:17px;}
  .bottom-q{font-size:17.3px;}
  .rule{position:absolute;border-top:1px dashed var(--rule);height:0;}
  .check{display:inline-flex;align-items:center;font-size:16.8px;}
  .box{display:inline-block;width:18px;height:18px;border:1.5px solid var(--ink);margin-left:3px;box-sizing:border-box;}
  .turnover{font-size:13.6px;}
</style>
</head>
<body>
<main class="form-page">

  <p class="brand-name">Harbour Dental</p>

  <address class="practice-address">
    HARBOUR DENTAL<br>4.07/88 SEAVIEW RD<br>KELSO BAY NSW2261<br>(02) 49 555 012
  </address>

  <h1 class="at form-title" style="top:236px;left:35px">CONFIDENTIAL MEDICAL HISTORY</h1>

  <!-- Patient details -->
  <span class="at" style="top:310px;left:35px">Name</span><span class="at" style="top:310px;left:127px">:</span><div class="rule" style="top:312px;left:146px;width:269px"></div>
  <span class="at" style="top:332px;left:35px">Address</span><span class="at" style="top:332px;left:127px">:</span><div class="rule" style="top:334px;left:146px;width:269px"></div>
  <div class="rule" style="top:358px;left:146px;width:269px"></div>
  <span class="at" style="top:377px;left:35px">Email</span><span class="at" style="top:377px;left:127px">:</span><div class="rule" style="top:386px;left:146px;width:269px"></div>
  <span class="at" style="top:399px;left:35px">Work No.</span><span class="at" style="top:399px;left:127px">:</span><div class="rule" style="top:410px;left:146px;width:269px"></div>
  <span class="at" style="top:422px;left:35px">Home No.</span><span class="at" style="top:422px;left:127px">:</span><div class="rule" style="top:434px;left:146px;width:269px"></div>
  <span class="at" style="top:444px;left:35px">Mobile No.</span><span class="at" style="top:444px;left:127px">:</span><div class="rule" style="top:458px;left:146px;width:269px"></div>

  <h2 class="at section-title" style="top:483px;left:35px">EMERGENCY CONTACT PERSON</h2>
  <span class="at" style="top:513px;left:35px">Name</span><span class="at" style="top:513px;left:130px">:</span><div class="rule" style="top:519px;left:146px;width:269px"></div>
  <span class="at" style="top:536px;left:35px">Relationship :</span><div class="rule" style="top:544px;left:146px;width:269px"></div>
  <span class="at" style="top:558px;left:35px">Phone No.</span><span class="at" style="top:558px;left:130px">:</span><div class="rule" style="top:569px;left:146px;width:269px"></div>

  <!-- General practitioner -->
  <h2 class="at section-title" style="top:273px;left:434px">GENERAL PRACTITIONER</h2>
  <span class="at gp" style="top:308px;left:434px">Name</span><span class="at gp" style="top:304px;left:557px">:</span><div class="rule" style="top:312px;left:570px;width:244px"></div>
  <span class="at gp" style="top:330px;left:434px">Practice Name :</span><div class="rule" style="top:336px;left:570px;width:244px"></div>
  <span class="at gp" style="top:353px;left:434px">Phone No.</span><span class="at gp" style="top:357px;left:557px">:</span><div class="rule" style="top:362px;left:570px;width:244px"></div>
  <span class="at gp" style="top:377px;left:434px">Do you have a Health Fund with Dental Cover ?</span>
  <span class="at check gp" style="top:402px;left:434px">Yes<span class="box" style="margin-left:8px"></span></span>
  <span class="at check gp" style="top:402px;left:504px">No<span class="box" style="margin-left:10px"></span></span>
  <span class="at gp" style="top:427px;left:434px">If so, what is the name of the Fund?</span>
  <div class="rule" style="top:458px;left:434px;width:380px"></div>
  <span class="at gp" style="top:472px;left:434px">Fund Number ?</span>
  <div class="rule" style="top:501px;left:434px;width:380px"></div>
  <span class="at gp" style="top:518px;left:434px">Priority Number on Card :</span>
  <span class="at gp" style="top:518px;left:649px">0</span><span class="at gp" style="top:518px;left:675px">1</span><span class="at gp" style="top:518px;left:701px">2</span><span class="at gp" style="top:518px;left:728px">3</span><span class="at gp" style="top:518px;left:754px">4</span><span class="at gp" style="top:518px;left:785px">5</span>
  <span class="at gp" style="top:540px;left:434px">Occupation</span><span class="at gp" style="top:540px;left:557px">:</span><div class="rule" style="top:546px;left:570px;width:244px"></div>
  <span class="at gp" style="top:563px;left:434px">Referred by</span><span class="at gp" style="top:563px;left:557px">:</span><div class="rule" style="top:570px;left:570px;width:244px"></div>

  <!-- Allergies -->
  <p class="at question" style="top:612px;left:35px">Please indicate if&nbsp; you are allergic to any of the following :</p>
  <span class="at check" style="top:642px;left:37px">Aspirin<span class="box"></span></span>
  <span class="at check" style="top:642px;left:120px">Codein<span class="box"></span></span>
  <span class="at check" style="top:642px;left:213px">Penicillin<span class="box"></span></span>
  <span class="at check" style="top:642px;left:313px">Sulfites<span class="box"></span></span>
  <span class="at check" style="top:642px;left:399px">Latex<span class="box"></span></span>
  <span class="at check" style="top:642px;left:478px">Local Anaesthetic<span class="box"></span></span>
  <span class="at check" style="top:642px;left:648px">Lactose<span class="box"></span></span>
  <span class="at check" style="top:642px;left:741px">Nickel<span class="box"></span></span>
  <span class="at" style="top:670px;left:38px">Other :</span><div class="rule" style="top:676px;left:94px;width:713px"></div>
  <div class="rule" style="top:702px;left:35px;width:772px"></div>

  <!-- Medication -->
  <p class="at question" style="top:727px;left:35px">Are you currently taking, or have ever taken, any of the following medication ?</p>
  <span class="at check" style="top:761px;left:37px">Asthma inhaler<span class="box"></span></span>
  <span class="at check" style="top:761px;left:198px">Anti-epileptics<span class="box"></span></span>
  <span class="at check" style="top:761px;left:364px">Anti-depressants<span class="box"></span></span>
  <span class="at check" style="top:761px;left:533px">Blood Pressure<span class="box"></span></span>
  <span class="at check" style="top:761px;left:684px">Blood Thinners<span class="box"></span></span>
  <span class="at check" style="top:791px;left:36px">Bisphosphonates<span class="box"></span></span>
  <span class="at check" style="top:791px;left:229px">Chemotherapy<span class="box"></span></span>
  <span class="at check" style="top:791px;left:409px">Insulin<span class="box"></span></span>
  <span class="at check" style="top:791px;left:520px">Immunosuppressants<span class="box"></span></span>
  <span class="at check" style="top:791px;left:730px">Steroids<span class="box"></span></span>
  <span class="at check" style="top:819px;left:37px">Oral Contraceptive<span class="box"></span></span>
  <span class="at check" style="top:819px;left:229px">Other<span class="box"></span></span>
  <span class="at hint" style="top:846px;left:36px">Please specify medication name, dose, and frequency where possible:</span>
  <div class="rule" style="top:882px;left:35px;width:780px"></div>
  <div class="rule" style="top:910px;left:35px;width:780px"></div>
  <div class="rule" style="top:936px;left:35px;width:780px"></div>
  <div class="rule" style="top:963px;left:35px;width:780px"></div>

  <!-- Antibiotic cover, joints, pregnancy -->
  <span class="at bottom-q" style="top:1005px;left:36px">Do you require antibiotic cover ?</span>
  <span class="at check bottom-q" style="top:1005px;left:318px">Yes<span class="box" style="margin-left:6px"></span></span>
  <span class="at check bottom-q" style="top:1005px;left:388px">No<span class="box" style="margin-left:8px"></span></span>
  <span class="at bottom-q" style="top:1034px;left:36px">Have you had a joint replacement ?</span>
  <span class="at check bottom-q" style="top:1034px;left:318px">Yes<span class="box" style="margin-left:6px"></span></span>
  <span class="at check bottom-q" style="top:1034px;left:388px">No<span class="box" style="margin-left:8px"></span></span>
  <span class="at bottom-q" style="top:1068px;left:36px">Women:</span>
  <span class="at bottom-q" style="top:1083px;left:36px">Are you pregnant ?</span>
  <span class="at check bottom-q" style="top:1083px;left:211px">Yes<span class="box" style="margin-left:6px"></span></span>
  <span class="at check bottom-q" style="top:1083px;left:282px">No<span class="box" style="margin-left:8px"></span></span>
  <span class="at check bottom-q" style="top:1083px;left:353px">Possible<span class="box" style="margin-left:8px"></span></span>
  <span class="at bottom-q" style="top:1083px;left:542px">Breast Feeding ?</span>
  <span class="at check bottom-q" style="top:1083px;left:687px">Yes<span class="box" style="margin-left:6px"></span></span>
  <span class="at check bottom-q" style="top:1083px;left:757px">No<span class="box" style="margin-left:10px"></span></span>

  <span class="at turnover" style="top:1162px;right:32px">Please Turnover</span>
</main>
</body>
</html>
```